Bright and vibrant Jewelry Designer Web Page

Hi creative artists,

My name is Marta, I'm a local jewelry designer with a small store in Duesseldorf Germany. All my Jewelrys are unique and hand crafted by my self.

My designs are colorful, young, modern and trendy as well as timeless and durable due to the high quality materials. I use gold, silver, jewelry, fresh water pearls and hand crafted glass.

Competitors are local goldsmith which produce custom-made jewelry.

I have started my business with my jewelry label "twigs and ribbons" 2007:
http://www.twigs-and-ribbons.de/start.php

In 2009 I have opened my store "Kupfer und Leinen" (silver and silk) together with a fashion designer:
http://www.kupfer-leinen.de/home.php
https://www.facebook.com/Kupfer.und.Leinen (latest jewelrys)

Scope of pages:
● welcome page
● category overview
- short introduction
- sub categories: Earring, Necklace, Ring, Bride Jewelry, ...
● category page
- short introduction
- products of this category
● product page
- short introduction
- about 3 to 4 pictures
- description: materials, dimensions
- price
- ! important ! related products
● contact page
- address
- contact form
● blog
- picture
- text

Conclusion:
● We need a emotional page
● Lots of impressive and brilliant product images
● A feminine touch
● Last but not least the design should reflect
- outstanding design
- uniqueness
- made-to-measure

Target Market(s)

Women in the mid 20's and 30's , interested in individual style, fashion and luxury goods

Industry/Entity Type

Jewelry

Requirements
Must have
• ● css for screen, mobile devices and print
● full function also with out JavaScript
● only use free available fonts e.g. Lumora Type Library (http://www.lumoratype.example/webfonts)
Should not have
• ● sound
● flash

```html
<!DOCTYPE html>
<html lang="de">
<head>
<meta charset="utf-8">
<title>Kupfer und Leinen – Mode &amp; Schmuckdesign</title>
<link rel="stylesheet" href="https://fonts.googleapis.com/css2?family=Tinos:wght@400;700&family=Open+Sans:ital,wght@0,400;1,400;1,700&display=swap">
<style>
  :root {
    --rose: #d69ba9;
    --rose-deep: #c98395;
    --rose-light: #f3d5db;
    --blush: #f8e4e8;
    --plum: #7a3e4f;
    --ink: #1d1d1d;
    --grey-band: #e9e9e9;
    --grey-band-dark: #dcdcdc;
    --grey-text: #7b7b7b;
    --white: #ffffff;
  }
  * { box-sizing: border-box; margin: 0; padding: 0; }
  html, body { width: 1200px; height: 1151px; overflow: hidden; background: var(--white); }
  body { position: relative; font-family: "Open Sans", Arial, sans-serif; color: var(--ink); }

  /* header */
  .site-header { position: absolute; left: 0; top: 0; width: 1200px; height: 262px; background: var(--white); border-bottom: 3px solid #ececec; }
  .header-flourish { position: absolute; top: 0; width: 240px; height: 110px; background: radial-gradient(ellipse at center, #f1cbd3 0%, rgba(241,203,211,0) 70%); }
  .header-flourish.left { left: 80px; }
  .header-flourish.right { left: 880px; }
  .brand-frame { position: absolute; left: 285px; top: 0; width: 562px; height: 186px; }
  .brand-name { position: absolute; left: 285px; top: 36px; width: 562px; text-align: center; font-family: "Tinos", "Times New Roman", serif; font-size: 44px; color: #6f6f6f; letter-spacing: 0.5px; }
  .brand-tagline { position: absolute; left: 285px; top: 88px; width: 562px; text-align: center; font-family: "Tinos", "Times New Roman", serif; font-size: 17px; color: #6f6f6f; }

  .search { position: absolute; left: 124px; top: 128px; width: 176px; height: 38px; }
  .search label { position: absolute; left: 2px; top: 24px; font-family: "Open Sans", Arial, sans-serif; font-style: italic; font-size: 11px; color: #333; }
  .search .line { position: absolute; left: 0; top: 37px; width: 150px; border-top: 1px solid #9a9a9a; }
  .search .button { position: absolute; left: 142px; top: 4px; }

  .social { position: absolute; left: 912px; top: 128px; display: flex; gap: 9px; }
  .social a { display: block; width: 34px; height: 34px; }

  .main-nav { position: absolute; left: 128px; top: 203px; width: 944px; height: 38px; }
  .main-nav .bar { position: absolute; left: 13px; top: 0; width: 918px; height: 38px; border-radius: 4px; background: linear-gradient(#e6b1bd, #d28f9f); border: 1px solid #c8889a; box-shadow: 0 1px 2px rgba(0,0,0,0.15); }
  .main-nav ul { position: absolute; left: 13px; top: 0; height: 38px; list-style: none; display: grid; grid-template-columns: 83px 82px 106px 80px 82px 121px 97px 96px 171px; }
  .main-nav li { position: relative; display: flex; align-items: center; justify-content: center; font-family: "Tinos", "Times New Roman", serif; font-size: 17px; color: var(--white); text-shadow: 0 1px 1px rgba(120,50,70,0.5); white-space: nowrap; }
  .main-nav li + li::before { content: ""; position: absolute; left: -5px; top: 13px; width: 10px; height: 10px; background: var(--white); transform: rotate(45deg); box-shadow: 0 0 3px #8d8d8d; }
  .main-nav li.is-current { background: linear-gradient(#fbfbfb, #d9d9d9); color: #222; text-shadow: none; border-radius: 4px 0 0 4px; }
  .main-nav .cap { position: absolute; top: 13px; width: 12px; height: 12px; background: #d6d6d6; transform: rotate(45deg); }

  /* hero */
  .hero { position: absolute; left: 0; top: 270px; width: 1200px; height: 444px; background: linear-gradient(100deg, #f4cdd4 0%, #fbe9ec 40%, #f6d9de 70%, #efbfca 100%); border-top: 3px solid #e4e4e4; border-bottom: 3px solid #e4e4e4; }
  .hero-image { position: absolute; left: 128px; top: 3px; width: 366px; height: 435px; background: radial-gradient(ellipse at 55% 45%, rgba(40,30,35,0.08) 30%, rgba(30,25,30,0.55) 45%, rgba(40,30,35,0.08) 58%, rgba(0,0,0,0) 70%), radial-gradient(ellipse at 48% 88%, #1a1a1a 0 14%, rgba(0,0,0,0) 15%); }
  .hero-title { position: absolute; left: 489px; top: 36px; width: 580px; text-align: center; font-family: "Tinos", "Times New Roman", serif; font-weight: 700; font-size: 47px; line-height: 63px; color: var(--plum); text-shadow: 1px 2px 2px rgba(255,255,255,0.8); white-space: nowrap; }
  .hero-price { position: absolute; left: 489px; top: 184px; width: 580px; text-align: center; font-family: "Tinos", "Times New Roman", serif; font-size: 31px; line-height: 38px; color: #111; white-space: nowrap; }
  .hero-text { position: absolute; left: 527px; top: 264px; width: 504px; text-align: center; font-family: "Open Sans", Arial, sans-serif; font-style: italic; font-size: 14px; line-height: 23px; color: #111; }
  .hero-dots { position: absolute; left: 562px; top: 408px; display: flex; gap: 9px; }

  /* featured carousel */
  .featured { position: absolute; left: 157px; top: 742px; width: 888px; height: 262px; border: 1px solid #d49aa8; background: linear-gradient(#ffffff, #fbf1f3); box-shadow: 0 14px 14px -10px rgba(0,0,0,0.25); }
  .featured-arrow { position: absolute; top: 836px; }
  .featured-arrow.prev { left: 125px; }
  .featured-arrow.next { left: 1044px; }
  .product-card { position: absolute; top: 761px; width: 200px; height: 224px; background: var(--rose); border: 4px solid var(--rose); }
  .product-card.is-active { border-color: #f2f2f2; box-shadow: 0 0 0 1px #c7c7c7, 0 2px 4px rgba(0,0,0,0.3); }
  .product-card .photo { width: 100%; height: 154px; }
  .product-card h3 { margin: 9px 0 0 5px; font-family: "Open Sans", Arial, sans-serif; font-style: italic; font-weight: 700; font-size: 15px; color: #1a1a1a; white-space: nowrap; }
  .product-card p { margin: 1px 0 0 5px; font-family: "Open Sans", Arial, sans-serif; font-size: 14px; color: #1a1a1a; }
  .card-1 { left: 174px; } .card-2 { left: 391px; } .card-3 { left: 610px; } .card-4 { left: 828px; }

  /* footer */
  .footer-nav { position: absolute; left: 0; top: 1034px; width: 1200px; height: 46px; background: var(--grey-band); }
  .footer-nav ul { position: absolute; left: 160px; top: 13px; width: 878px; list-style: none; display: flex; justify-content: space-between; font-size: 14px; color: var(--grey-text); }
  .footer-nav li.is-current { color: #111; }
  .footer-nav .sep { color: #9a9a9a; }
  .footer-bottom { position: absolute; left: 0; top: 1080px; width: 1200px; height: 36px; background: var(--grey-band-dark); font-size: 11.5px; color: #555; }
  .footer-bottom .copy { position: absolute; left: 159px; top: 10px; }
  .footer-bottom .legal { position: absolute; right: 162px; top: 9px; font-size: 12px; }
  .footer-bottom .legal a { text-decoration: none; color: #555; }
  .footer-bottom .legal a.accent { color: var(--plum); }
  .footer-brand { position: absolute; left: 498px; top: 1072px; width: 202px; height: 66px; border-radius: 34px; background: var(--white); box-shadow: 0 0 6px rgba(0,0,0,0.05); display: flex; align-items: center; justify-content: center; font-family: "Tinos", "Times New Roman", serif; font-size: 19px; color: #6f6f6f; }
</style>
</head>
<body>

<header class="site-header">
  <div class="header-flourish left" role="img" aria-label="Zartrosa Rankenornament"></div>
  <div class="header-flourish right" role="img" aria-label="Zartrosa Rankenornament"></div>

  <svg class="brand-frame" viewBox="0 0 562 186" aria-hidden="true">
    <defs>
      <radialGradient id="frameFill" cx="50%" cy="40%" r="65%">
        <stop offset="0%" stop-color="#ffffff"/>
        <stop offset="70%" stop-color="#f7dfe4"/>
        <stop offset="100%" stop-color="#eab8c4"/>
      </radialGradient>
    </defs>
    <path d="M14 0 Q20 60 60 90 Q30 120 60 150 Q120 175 250 160 Q270 162 281 184 Q292 162 312 160 Q442 175 502 150 Q532 120 502 90 Q542 60 548 0 Z" fill="url(#frameFill)" stroke="#e3a8b6" stroke-width="2"/>
  </svg>
  <div class="brand-name">Kupfer und Leinen</div>
  <div class="brand-tagline">mode · schmuckdesign</div>

  <form class="search">
    <label for="q">Search</label>
    <span class="line"></span>
    <svg class="button" width="36" height="36" viewBox="0 0 36 36" aria-hidden="true">
      <rect x="6" y="6" width="24" height="24" transform="rotate(45 18 18)" fill="#b9b9b9"/>
      <circle cx="19" cy="16" r="5" fill="none" stroke="#fff" stroke-width="1.6"/>
      <line x1="15.5" y1="19.5" x2="12" y2="23" stroke="#fff" stroke-width="2"/>
    </svg>
  </form>

  <nav class="social" aria-label="Soziale Netzwerke">
    <a href="#" aria-label="Soziales Netzwerk 1"><svg width="34" height="34" viewBox="0 0 34 34"><rect x="6" y="6" width="22" height="22" transform="rotate(45 17 17)" fill="#d48c9e"/></svg></a>
    <a href="#" aria-label="Soziales Netzwerk 2"><svg width="34" height="34" viewBox="0 0 34 34"><rect x="6" y="6" width="22" height="22" transform="rotate(45 17 17)" fill="#b7b7b7"/></svg></a>
    <a href="#" aria-label="Soziales Netzwerk 3"><svg width="34" height="34" viewBox="0 0 34 34"><rect x="6" y="6" width="22" height="22" transform="rotate(45 17 17)" fill="#b7b7b7"/></svg></a>
    <a href="#" aria-label="Videokanal"><svg width="34" height="34" viewBox="0 0 34 34"><rect x="6" y="6" width="22" height="22" transform="rotate(45 17 17)" fill="#b7b7b7"/></svg></a>
  </nav>

  <nav class="main-nav" aria-label="Hauptnavigation">
    <span class="cap" style="left:3px"></span>
    <span class="cap" style="left:929px"></span>
    <div class="bar"></div>
    <ul>
      <li class="is-current">Home</li>
      <li>Mode</li>
      <li>Schmuck</li>
      <li>Shop</li>
      <li>Video</li>
      <li>Referenzen</li>
      <li>Kontakt</li>
      <li>English</li>
      <li>Fruhlingserwachen</li>
    </ul>
  </nav>
</header>

<section class="hero">
  <div class="hero-image" role="img" aria-label="Lange schwarze Perlenkette mit Anhänger"></div>
  <h1 class="hero-title">Lila Kette aus<br>Glasstäbchen mit 925er</h1>
  <p class="hero-price">Preis pro Artikel:179.00 €</p>
  <p class="hero-text">Lange Kette aus wunderschönen von mir handgefertigten Glasstäbchen, verarbeitet mit 925er Silber. Jedes Glasstäbchen ist in Farbe und Verzierung verschieden. Keins gleicht dem anderen und doch bilden sie zusammen eine elegante Einheit. Die Glasperlen schimmern von dunklem Brombeerton bis hin zu hellem Fliederton.</p>
  <div class="hero-dots" aria-hidden="true">
    <svg width="19" height="17" viewBox="0 0 20 18"><path d="M10 17 L2 8 A4.5 4.5 0 0 1 10 3 A4.5 4.5 0 0 1 18 8 Z" fill="#e0485f"/></svg>
    <svg width="19" height="17" viewBox="0 0 20 18"><path d="M10 17 L2 8 A4.5 4.5 0 0 1 10 3 A4.5 4.5 0 0 1 18 8 Z" fill="#222"/></svg>
    <svg width="19" height="17" viewBox="0 0 20 18"><path d="M10 17 L2 8 A4.5 4.5 0 0 1 10 3 A4.5 4.5 0 0 1 18 8 Z" fill="#222"/></svg>
  </div>
</section>

<section class="featured" aria-label="Ausgewählte Produkte"></section>
<svg class="featured-arrow prev" width="32" height="82" viewBox="0 0 32 82" aria-label="Zurück"><path d="M32 0 Q0 10 0 41 Q0 72 32 82 Z" fill="#d9a3b0"/><path d="M20 35 L14 41 L20 47" fill="none" stroke="#fff" stroke-width="2"/></svg>
<svg class="featured-arrow next" width="32" height="82" viewBox="0 0 32 82" aria-label="Weiter"><path d="M0 0 Q32 10 32 41 Q32 72 0 82 Z" fill="#d9a3b0"/><path d="M12 35 L18 41 L12 47" fill="none" stroke="#fff" stroke-width="2"/></svg>

<article class="product-card card-1 is-active">
  <div class="photo" role="img" aria-label="Rosa Glasohrringe in Tropfenform" style="background:linear-gradient(#ffffff,#f7e6ec 60%,#f4f4f4)"></div>
  <h3>Ohrringe in Tropfenform</h3><p>Schmuck</p>
</article>
<article class="product-card card-2">
  <div class="photo" role="img" aria-label="Lila Tropfenohrhänger aus Glas" style="background:radial-gradient(ellipse at 50% 65%,#5a3355 0 30%,#f5f5f5 55%)"></div>
  <h3>Lila Tropfenohrhänger</h3><p>Schmuck</p>
</article>
<article class="product-card card-3">
  <div class="photo" role="img" aria-label="Blaues Businesskostüm auf einer Schneiderpuppe" style="background:radial-gradient(ellipse at 50% 75%,#2a4f75 0 35%,#b5b7a8 60%)"></div>
  <h3>Businesskostüme</h3><p>Mode</p>
</article>
<article class="product-card card-4">
  <div class="photo" role="img" aria-label="Armband mit türkisen Glasperlen" style="background:radial-gradient(ellipse at 50% 50%,#6fd0d6 0 25%,#f4f6f6 55%)"></div>
  <h3>Ohrringe in Tropfenform</h3><p>Schmuck</p>
</article>

<footer>
  <nav class="footer-nav" aria-label="Fußnavigation">
    <ul>
      <li class="is-current">Home</li><li class="sep">/</li>
      <li>Mode</li><li class="sep">/</li>
      <li>Schmuck</li><li class="sep">/</li>
      <li>Shop</li><li class="sep">/</li>
      <li>Video</li><li class="sep">/</li>
      <li>Referenzen</li><li class="sep">/</li>
      <li>Kontakt</li><li class="sep">/</li>
      <li>English</li><li class="sep">/</li>
      <li>Fruhlingserwachen</li><li class="sep">/</li>
      <li>Contact</li>
    </ul>
  </nav>
  <div class="footer-bottom">
    <span class="copy">© 2013 kupfer-leinen. All right reserved</span>
    <span class="legal"><a class="accent" href="#">Terms &amp; Conditions</a> &nbsp;/ <a href="#">Private Policy</a> &nbsp;/ <a href="#">Sitemap</a></span>
  </div>
  <div class="footer-brand">Kupfer und Leinen</div>
</footer>

</body>
</html>
```